mobile app maker needs website redone

We currently have a running website that generates some traffic and looks ok but now we want to revamp it with professional modern eye catching design.
We are open to proposals and open to any new ideas or suggestions but we have to see your previous work.
our current site is www.drelvaapp.com

Industry/Entity Type

It Professional

Coding

Coded - Design and coding required

Number of Pages Required

5+ page

Font styles to use
Serif
Other font styles liked:
• open

Requirements
Must have
• modern look and feel easy to use
Nice to have
• responsive websites , example are as follow ,http://quorpa-layout.pagemint.site , vantri.com , http://saddex.pagemint.site

```html
<!DOCTYPE html>
<html lang="en">
<head>
<meta charset="utf-8">
<title>Drelva Marketing – Mobile Apps &amp; Mobile Websites</title>
<link rel="stylesheet" href="https://fonts.googleapis.com/css2?family=Montserrat:wght@500;700&family=Open+Sans:wght@400;600;700&display=swap">
<style>
:root{
  --ink:#111111;
  --navy:#0b2a4a;
  --teal:#123f45;
  --muted:#555555;
  --white:#ffffff;
  --footer:#050505;
  --footer-text:#d9d9d9;
  --rule:#444444;
}
*{box-sizing:border-box;margin:0;padding:0}
html,body{width:1200px;height:1200px;overflow:hidden;background:var(--white)}
body{position:relative;font-family:"Open Sans",sans-serif;color:var(--ink)}
.abs{position:absolute}
.site-header{top:0;left:0;width:1200px;height:64px;border-top:2px solid var(--ink);background:var(--white)}
.brand{left:125px;top:34px;display:flex;align-items:center;gap:8px;font-family:"Montserrat",sans-serif;font-weight:500;font-size:19px;line-height:22px;color:var(--ink)}
.brand-mark{width:12px;height:12px;background:var(--ink)}
.main-nav{top:16px;left:367px;display:flex;align-items:center}
.main-nav a{font-family:"Open Sans",sans-serif;font-weight:600;font-size:10.5px;letter-spacing:.8px;color:var(--ink);text-decoration:none;text-transform:uppercase;padding:8px 14px;margin-right:24px}
.main-nav a.active{background:var(--ink);color:var(--white)}
.main-nav a.login{background:var(--navy);color:var(--white);margin-left:10px;margin-right:0;padding:8px 18px}
.hero{top:64px;left:0;width:1200px;height:362px;background:linear-gradient(180deg,#133c42,#175057)}
.hero-caption{left:251px;top:196px;width:698px;height:83px;background:rgba(20,40,44,.55);display:flex;flex-direction:column;justify-content:center;align-items:center;font-family:"Montserrat",sans-serif;font-weight:700;font-size:23px;letter-spacing:2.4px;color:var(--white);line-height:35px;text-transform:uppercase}
.intro-title{left:125px;top:440px;font-family:"Montserrat",sans-serif;font-weight:700;font-size:18px;letter-spacing:1.2px;text-transform:uppercase}
.intro-sub{left:126px;top:471px;font-weight:600;font-size:10px;letter-spacing:.95px;text-transform:uppercase}
.intro-copy{left:125px;top:494px;width:770px;font-size:11px;line-height:20.2px;letter-spacing:.85px;color:var(--muted)}
.intro-copy p+p{margin-top:20.2px}
.btn{display:inline-flex;align-items:center;justify-content:center;background:var(--navy);color:var(--white);font-family:"Montserrat",sans-serif;font-weight:700;font-size:10.5px;letter-spacing:1px;text-transform:uppercase;text-decoration:none}
.intro-btn{left:125px;top:666px;width:107px;height:30px}
.device-shot{left:918px;top:482px;width:158px;height:199px;background:linear-gradient(180deg,#1b1b1b,#2c4d78 50%,#1b1b1b)}
.features-title{left:126px;top:724px;font-family:"Montserrat",sans-serif;font-weight:700;font-size:12.5px;letter-spacing:1.2px;text-transform:uppercase}
.feature{top:762px;width:240px;text-align:center}
.feature svg{display:block;margin:0 auto;overflow:visible}
.feature h3{margin-top:12px;font-family:"Montserrat",sans-serif;font-weight:700;font-size:10.5px;letter-spacing:1.2px;text-transform:uppercase}
.feature p{margin-top:11px;font-size:10.6px;line-height:17.6px;letter-spacing:.6px;color:var(--muted)}
.feature .btn{margin-top:14px;width:107px;height:29px}
.site-footer{top:984px;left:0;width:1200px;height:216px;background:var(--footer);color:var(--footer-text)}
.footer-col{top:16px;width:230px}
.footer-col h4{font-family:"Montserrat",sans-serif;font-weight:700;font-size:12.5px;letter-spacing:1.4px;color:var(--white);text-transform:uppercase;margin-bottom:10px}
.footer-col p,.footer-col li{font-size:10.8px;line-height:17.5px;letter-spacing:.85px}
.footer-col.about{width:212px}
.footer-col ul{list-style:none}
.footer-col li{line-height:26px}
.footer-col strong{color:var(--white);font-weight:700}
.footer-btn{margin-top:12px;width:91px;height:28px;background:var(--white);color:var(--ink)}
.footer-rule{left:124px;top:176px;width:952px;height:1px;background:var(--rule)}
.copyright{left:0;top:187px;width:1200px;text-align:center;font-size:9.8px;letter-spacing:.6px}
</style>
</head>
<body>
<header class="site-header abs">
  <div class="brand abs"><span class="brand-mark"></span>Drelva Marketing</div>
  <nav class="main-nav abs">
    <a class="active">Home</a><a>Features</a><a>Pricing</a><a>Contact</a><a>Skipper</a><a>Preview your app</a><a class="login">Login</a>
  </nav>
</header>

<section class="hero abs" role="img" aria-label="Flat illustration of hands holding smartphones showing shopping, ideas, global and chat apps">
</section>
<div class="hero-caption abs"><span>Welcome to the revolution</span><span>Mobile apps &amp; mobile websites made easy!</span></div>

<h1 class="intro-title abs">Welcome to our Drelva Inc.</h1>
<h2 class="intro-sub abs">We provide the easiest way for businesses to create mobile apps!</h2>
<div class="intro-copy abs">
  <p>Consumers use their mobile devices to find the information they want, as soon as they want it. They depend on the instant accessib ility of mobile apps to quickly tell them what they need to know, so they can make their purchasing decisions and get on with what they’re doing.</p>
  <p>Smart business owners understand the power and importance of mobile marketing to their bottom line. They use mobile apps to connect with customers, share relevant news, offer great deals, increase foot traffic, take reservations, and boost their revenues. Whether they deliver a service, sell products in a store, or run a successful restaurant, they know that having a mobile app is one of the most effective ways to reach their customers, whether they’re on the go or standing still.</p>
</div>
<a class="btn intro-btn abs">Read more</a>
<div class="device-shot abs" role="img" aria-label="Smartphone lock screen showing the time, a news notification over an earth wallpaper and a slide to unlock bar"></div>

<h2 class="features-title abs">We provide the easiest way for businesses to create mobile apps!</h2>

<div class="feature abs" style="left:114px">
  <svg width="74" height="64" viewBox="0 0 74 64"><ellipse cx="37" cy="32" rx="35.5" ry="30.5" fill="none" stroke="#0b2a4a" stroke-width="1.6"/><circle cx="37" cy="32" r="3.5" fill="#111"/><path d="M30 25a10 10 0 0 0 0 14M44 25a10 10 0 0 1 0 14M25 20a17 17 0 0 0 0 24M49 20a17 17 0 0 1 0 24" fill="none" stroke="#111" stroke-width="3.2" stroke-linecap="round"/></svg>
  <h3>Preview online</h3><p>We allow you to preview your apps<br>as we build it.</p><a class="btn">Read more</a>
</div>
<div class="feature abs" style="left:358px">
  <svg width="74" height="64" viewBox="0 0 74 64"><ellipse cx="37" cy="32" rx="35.5" ry="30.5" fill="none" stroke="#0b2a4a" stroke-width="1.6"/><circle cx="37" cy="32" r="3.5" fill="#111"/><path d="M30 25a10 10 0 0 0 0 14M44 25a10 10 0 0 1 0 14M25 20a17 17 0 0 0 0 24M49 20a17 17 0 0 1 0 24" fill="none" stroke="#111" stroke-width="3.2" stroke-linecap="round"/></svg>
  <h3>Incredibly easy</h3><p>We allow you to preview your apps<br>as we build it.</p><a class="btn">Read more</a>
</div>
<div class="feature abs" style="left:603px">
  <svg width="74" height="64" viewBox="0 0 74 64"><ellipse cx="37" cy="32" rx="35.5" ry="30.5" fill="none" stroke="#0b2a4a" stroke-width="1.6"/><circle cx="37" cy="32" r="3.5" fill="#111"/><path d="M30 25a10 10 0 0 0 0 14M44 25a10 10 0 0 1 0 14M25 20a17 17 0 0 0 0 24M49 20a17 17 0 0 1 0 24" fill="none" stroke="#111" stroke-width="3.2" stroke-linecap="round"/></svg>
  <h3>Powerful hosting</h3><p>We allow you to preview your apps<br>as we build it.</p><a class="btn">Read more</a>
</div>
<div class="feature abs" style="left:847px">
  <svg width="74" height="64" viewBox="0 0 74 64"><ellipse cx="37" cy="32" rx="35.5" ry="30.5" fill="none" stroke="#0b2a4a" stroke-width="1.6"/><circle cx="37" cy="32" r="3.5" fill="#111"/><path d="M30 25a10 10 0 0 0 0 14M44 25a10 10 0 0 1 0 14M25 20a17 17 0 0 0 0 24M49 20a17 17 0 0 1 0 24" fill="none" stroke="#111" stroke-width="3.2" stroke-linecap="round"/></svg>
  <h3>Apps &amp; websitess</h3><p>We allow you to preview your apps<br>as we build it.</p><a class="btn">Read more</a>
</div>

<footer class="site-footer abs">
  <div class="footer-col about abs" style="left:124px">
    <h4>About Drelva Inc.</h4>
    <p>A Delaware Corporation The fast &amp; easy way for small businesses to create mobile applications whether they’re on the go or standing still.</p>
    <a class="btn footer-btn">Read more</a>
  </div>
  <div class="footer-col abs" style="left:370px">
    <h4>Quick links</h4>
    <ul><li>Features</li><li>Pricing</li><li>Skipper</li><li>Contact Us</li><li>Login</li></ul>
  </div>
  <div class="footer-col abs" style="left:614px">
    <h4>Social links</h4>
    <ul><li>Friendhub</li><li>Chirpline</li><li>Workweave</li><li>Searchly +</li><li>Clipstream</li></ul>
  </div>
  <div class="footer-col abs" style="left:859px">
    <h4>Contact us</h4>
    <p><strong>Address :</strong><br>418, Marrow Lane, Fenwick, 054, US<br>New York</p>
    <p style="margin-top:17px"><strong>Phone :</strong><br>555-018-3346</p>
  </div>
  <div class="footer-rule abs"></div>
  <p class="copyright abs">Copyright 2014 admin@drelvaapp.com- Mobile apps &amp; mobile websites for small businesses</p>
</footer>
</body>
</html>
```